Business Card For Video Production Company

Please NOTE: I've added some info to the must haves that I should have included at the start. Thank you.

I need a business card design for my video production company based in Orlando called Caldera Film Works. Our work consists of web video marketing (web videos), training videos, sales videos, conference and seminar video production...basically a lot of corporate based work.

We work with successful small businesses, not-for-profits and some Fortune 500 type groups. We bring a lot of knowledge, experience and attention to detail to every project.

I'd like something that communicates strength, confidence, integrity, as well as creative vision. I want to stay away from the standard icons of the media and film industry. I'd like to emphasize the colors of my logo, and also the colors of my website which has a white background. Simple is good.

Our budgets are moderate...generally $1500 to $5000.

www.calderafilm.tv

PS...We don't do weddings or recitals, or that type of production.
Updates

I want to thank all the designers for your updates. There's way too many to be able to give feedback on for all. I hope you understand that. But wow…there are so many great designs everyone has offered. I can't thank you enough…each and everyone. I hope to make my decision soon. I'm not accepting anymore designs from new designers. Brent-

Target Market(s)

Successful small businesses, marketing directors, corporate communication directors, training and human resources professionals. forward thinking not-for profits. Since my company is based in Central Florida, most of my work comes from this area too.

Industry/Entity Type

Marketing

Requirements
Must have
• website address, www.calderafilm.tv
phone number, 407-552-9031
email address, brent@calderafilm.tv

Title
Brent Caldera
Owner/Creative Director

I'd like to have a single line that goes across illustrating our services, maybe separated with bullet points:

Marketing Videos, Corporate Videos, Conference & Seminar Video Production
Should not have
• No film or video icons.
No need to pull language or copy from my website.

```html
<!DOCTYPE html>
<html lang="en">
<head>
<meta charset="utf-8">
<title>Caldera Film Works – Business Card</title>
<link href="https://fonts.googleapis.com/css2?family=Damion&family=Montserrat:wght@600&family=Arimo:wght@400;700&display=swap" rel="stylesheet">
<style>
  :root {
    --page: #ffffff;
    --brand-blue: #1f5ff0;
    --brand-blue-soft: rgba(31, 95, 240, 0.85);
    --brand-blue-faint: rgba(31, 95, 240, 0.22);
    --card-border: #2b63e6;
    --deep-navy: #0a1d55;
    --ink: #111111;
    --logo-grey: #3f4a50;
    --strip-tint: rgba(200, 200, 200, 0.35);
    --strip-tint-dark: rgba(255, 255, 255, 0.08);
    --white: #ffffff;
  }
  * { margin: 0; padding: 0; box-sizing: border-box; }
  html, body {
    width: 1200px; height: 900px; overflow: hidden;
    background: var(--page);
    font-family: "Arimo", Arial, sans-serif;
  }
  .canvas { position: relative; width: 1200px; height: 900px; }

  /* Front */
  .card-front {
    position: absolute; left: 153px; top: 40px;
    width: 713px; height: 386px;
    border: 3px solid var(--card-border);
    background: var(--white);
    overflow: hidden;
  }
  .front-strip {
    position: absolute; left: -60px; top: 150px;
    width: 420px; height: 70px;
    background: linear-gradient(90deg, transparent, var(--strip-tint), transparent);
    transform: rotate(-45deg);
  }
  .hero-art {
    position: absolute; left: 305px; top: 0;
    width: 408px; height: 386px;
    background: radial-gradient(circle at 200px 103px,
      var(--brand-blue) 0,
      var(--brand-blue-soft) 95px,
      var(--brand-blue-faint) 200px,
      transparent 260px);
  }
  .company-name {
    position: absolute; left: 10px; top: 158px;
    display: flex; align-items: center; gap: 10px;
    font-family: "Montserrat", Arial, sans-serif;
    font-weight: 600; font-size: 25px; color: var(--logo-grey);
    letter-spacing: -0.3px;
  }
  .company-name .mark {
    width: 38px; height: 38px; background: var(--brand-blue);
  }
  .person-name {
    position: absolute; left: 115px; top: 238px;
    font-family: "Damion", cursive;
    font-size: 46px; color: var(--ink); line-height: 1;
  }
  .person-title {
    position: absolute; left: 157px; top: 303px;
    font-size: 15px; color: var(--ink);
  }

  /* Back */
  .card-back {
    position: absolute; left: 410px; top: 461px;
    width: 718px; height: 391px;
    border: 2px solid var(--card-border);
    border-radius: 3px;
    padding: 3px;
    background: var(--white);
  }
  .back-face {
    position: relative; width: 100%; height: 100%;
    background: linear-gradient(90deg, var(--brand-blue) 0%, var(--brand-blue) 64%, #1240b8 80%, var(--deep-navy) 100%);
    overflow: hidden;
    color: var(--white);
    text-align: center;
  }
  .back-strip {
    position: absolute; width: 90px; height: 520px;
    background: var(--strip-tint-dark);
    transform: rotate(45deg);
  }
  .back-strip.left { left: 80px; top: -110px; }
  .back-strip.right { left: 560px; top: 60px; }
  .services {
    position: absolute; left: 0; right: 0; top: 78px;
    font-size: 16.5px;
  }
  .contact-frame { position: absolute; left: 199px; top: 124px; }
  .contact-heading {
    position: absolute; left: 0; right: 0; top: 138px;
    font-weight: 700; font-size: 19px;
  }
  .contact-list {
    position: absolute; left: 0; right: 0; top: 196px;
    list-style: none; font-size: 18px; line-height: 30.5px;
  }
</style>
</head>
<body>
<main class="canvas">

  <section class="card-front">
    <div class="front-strip" role="img" aria-label="Faint diagonal film strip decoration"></div>
    <div class="hero-art" role="img" aria-label="Large blue film leader target graphic"></div>
    <div class="company-name"><span class="mark"></span>Caldera Film Works</div>
    <p class="person-name">Brent Caldera</p>
    <p class="person-title">Owner/Creative Director</p>
  </section>

  <section class="card-back">
    <div class="back-face">
      <div class="back-strip left" role="img" aria-label="Faint diagonal film strip decoration"></div>
      <div class="back-strip right" role="img" aria-label="Faint diagonal film strip decoration"></div>
      <p class="services">Marketing Videos, Corporate Videos, Conference &amp; Seminar Video Production</p>
      <svg class="contact-frame" width="306" height="184" viewBox="0 0 306 184" aria-hidden="true">
        <g fill="none" stroke="var(--white)" stroke-width="2">
          <polyline points="38,3 3,3 3,38"/>
          <polyline points="268,3 303,3 303,38"/>
          <polyline points="3,146 3,181 38,181"/>
          <polyline points="303,146 303,181 268,181"/>
        </g>
      </svg>
      <p class="contact-heading">Contact</p>
      <ul class="contact-list">
        <li>web: www.calderafilm.tv</li>
        <li>mobile: 407-552-9031</li>
        <li>email: brent@calderafilm.tv</li>
      </ul>
    </div>
  </section>

</main>
</body>
</html>
```